Tobin Quartz Portal Page . It's guarantee project!

We need a clean and professional modern web application portal page
That includes the Login & Application Selection screen

Also, I need to design both Desktop and Mobile sizes.
We have an example design for our target

The application is Jetty Schedule and related data.
Our client is a bit conservative.

Theme color preferred : #00508B (main) #DF0D83 (secondary)

Target Market(s)

Oil & Fuel & Gasoline

Number of Pages Required

2 page

Font styles to use
Sans Serif

Colors
0054AA
0677BA
7BADD7
CADEEF
E8F1F8
E54698
E96AAD
F1A4CE
F9D9EA
FCEFF6

Requirements
Must have
• Login Page & Main Screen

```html
<!DOCTYPE html>
<html lang="en">
<head>
<meta charset="utf-8">
<title>Tobin Quartz – Login</title>
<link rel="stylesheet" href="https://fonts.googleapis.com/css2?family=Roboto:wght@700&family=Montserrat:wght@400;500;700&display=swap">
<style>
  :root {
    --brand-blue: #00508B;
    --heading-blue: #0A4F93;
    --pink: #E54698;
    --pink-button: #E96AAD;
    --pink-tint: #FCEFF6;
    --ink: #262626;
    --ink-soft: #3F3F46;
    --field-bg: #F4F5F7;
    --field-border: #DADCE1;
    --placeholder: #8A8D93;
    --show-link: #C3C1E8;
    --tab-line: #E3E3E3;
    --white: #FFFFFF;
  }
  * { box-sizing: border-box; margin: 0; padding: 0; }
  html, body { width: 1200px; height: 3047px; overflow: hidden; background: var(--white); }
  .page { position: relative; width: 1200px; height: 3047px; overflow: hidden; font-family: "Montserrat", sans-serif; }
  .top-wave { position: absolute; top: 0; left: 0; width: 1200px; height: 500px; }
  .welcome-title {
    position: absolute; left: 178px; top: 395px;
    font-family: "Roboto", sans-serif; font-weight: 700;
    font-size: 128px; line-height: 158px; color: var(--heading-blue);
    letter-spacing: -1px;
  }
  .hero-illustration {
    position: absolute; left: 202px; top: 762px; width: 810px; height: 590px;
    background: linear-gradient(160deg, #F5F7F8 0%, #D9E4E8 35%, #1B9CB8 60%, #1A7F9C 80%, #D2D4D6 100%);
    clip-path: polygon(0 52%, 62% 8%, 100% 47%, 100% 60%, 38% 100%, 0 66%);
  }
  .auth-tabs { position: absolute; left: 152px; top: 1480px; display: flex; gap: 54px; }
  .auth-tab {
    font-size: 32px; font-weight: 500; color: var(--pink);
    padding-bottom: 26px; border-bottom: 4px solid var(--tab-line);
  }
  .auth-tab.is-active { border-bottom-color: var(--pink); }
  .auth-tab.signup { border-bottom-width: 2px; padding-bottom: 28px; }
  .login-card {
    position: absolute; left: 90px; top: 1665px; width: 1035px; height: 1232px;
    background: var(--pink-tint); border-radius: 18px;
    box-shadow: 0 8px 10px rgba(0,0,0,0.22);
  }
  .card-title {
    position: absolute; left: 94px; top: 20px;
    font-size: 96px; font-weight: 700; line-height: 120px; color: var(--ink);
  }
  .card-subtitle {
    position: absolute; left: 98px; top: 326px; width: 860px;
    font-size: 40px; line-height: 48px; color: var(--ink-soft);
  }
  .field {
    position: absolute; left: 94px; width: 799px; height: 115px;
    background: var(--field-bg); border: 2px solid var(--field-border); border-radius: 6px;
    display: flex; align-items: center; justify-content: space-between;
    padding: 0 48px; font-size: 30px; color: var(--placeholder);
  }
  .field-email { top: 610px; }
  .field-password { top: 812px; }
  .field-toggle { color: var(--show-link); }
  .login-button {
    position: absolute; left: 524px; top: 1021px; width: 369px; height: 115px;
    background: var(--pink-button); border-radius: 4px; color: var(--white);
    font-size: 34px; font-weight: 500; display: flex; align-items: center; justify-content: center;
  }
</style>
</head>
<body>
<main class="page">
  <svg class="top-wave" viewBox="0 0 1200 500" aria-hidden="true">
    <path fill="var(--brand-blue)" d="M40,0 C110,60 190,110 300,122 C400,132 480,142 570,110 C670,74 770,62 880,140 C960,200 1000,300 1040,380 C1080,450 1140,472 1200,486 L1200,0 Z"/>
  </svg>

  <h1 class="welcome-title">Welcome To<br>Tobin Quartz</h1>

  <div class="hero-illustration" role="img" aria-label="Isometric illustration of an offshore oil platform, tanker ship, storage tank, fuel truck and workers on a teal jetty"></div>

  <nav class="auth-tabs">
    <span class="auth-tab is-active">Login</span>
    <span class="auth-tab signup">Sign up</span>
  </nav>

  <section class="login-card">
    <h2 class="card-title">Get more things<br>done with us</h2>
    <p class="card-subtitle">Search Sourcing the world's brightest professionals for your business.</p>
    <div class="field field-email"><span>Email Address</span></div>
    <div class="field field-password"><span>Password</span><span class="field-toggle">Show</span></div>
    <div class="login-button">Login</div>
  </section>
</main>
</body>
</html>
```